BANNER FOR JOB FAIR

I need a graphic for a 33W x 81H retractable banner for a job fair.
The banner should use our branded colors and be attractive to people walking by. Some info to put on it:
Commercial Construction
Specializing in Historic Renovation and Urban Development

Start your career in construction with the creative team of Brisol

Maybe a place for a QR code

The final design should communicate that we are a company that is creative and unique and think outside the box. Fun and innovative.
Focusing on Downtown Jacksonville Florida. (doesn't necessarily need to have this)

```html
<!DOCTYPE html>
<html lang="en">
<head>
<meta charset="utf-8">
<title>Brisol Job Fair Banner</title>
<link rel="stylesheet" href="https://fonts.googleapis.com/css2?family=Oswald:wght@600&family=Roboto:wght@300;400;700&display=swap">
<style>
  :root {
    --navy: #2b4a6e;
    --navy-deep: #223d5c;
    --gold: #d6a92b;
    --ink: #1d1d1f;
    --paper: #ffffff;
    --backdrop: #e9e7e2;
    --photo-sky: #6f9bc9;
    --photo-ground: #a8876a;
  }
  * { margin: 0; padding: 0; box-sizing: border-box; }
  html, body {
    width: 1200px; height: 1200px; overflow: hidden;
    background: var(--backdrop);
  }
  .canvas { position: relative; width: 1200px; height: 1200px; }
  .banner {
    position: absolute; left: 370px; top: 80px;
    width: 461px; height: 1040px;
    background: var(--paper);
    overflow: hidden;
    box-shadow: 0 6px 24px rgba(0,0,0,0.12);
  }
  .banner-graphics { position: absolute; inset: 0; width: 461px; height: 1040px; }
  .brand {
    position: absolute; top: 22px; left: 0; width: 100%;
    text-align: center;
    font-family: "Roboto", sans-serif;
  }
  .brand-name {
    font-weight: 700; font-size: 46px; letter-spacing: 2px;
    color: var(--navy); line-height: 1;
  }
  .brand-tagline {
    margin-top: 8px;
    font-weight: 400; font-size: 10px; letter-spacing: 1px;
    color: var(--navy); text-transform: uppercase;
  }
  .headline {
    position: absolute; top: 148px; left: 0; width: 100%;
    text-align: center;
    font-family: "Oswald", sans-serif; font-weight: 600;
    text-transform: uppercase; line-height: 1.08;
  }
  .headline-top { display: block; font-size: 70px; color: var(--gold); letter-spacing: 1px; }
  .headline-bottom { display: block; font-size: 70px; color: var(--navy); letter-spacing: 0; }
  .specialty {
    position: absolute; top: 378px; left: 0; width: 100%;
    text-align: center;
    font-family: "Roboto", sans-serif; font-size: 24px; line-height: 32px;
    color: var(--ink);
  }
  .specialty-light { font-weight: 300; }
  .specialty-strong { font-weight: 700; }
  .career-call {
    position: absolute; top: 532px; left: 0; width: 100%;
    text-align: center;
    font-family: "Roboto", sans-serif; font-weight: 700;
    font-size: 27px; line-height: 31px;
    color: var(--navy);
  }
  .location {
    position: absolute; top: 965px; left: 0; width: 100%;
    text-align: center;
    font-family: "Roboto", sans-serif; font-weight: 700;
    font-size: 20px; color: var(--paper);
  }
</style>
</head>
<body>
<div class="canvas">
  <section class="banner">
    <svg class="banner-graphics" viewBox="0 0 461 1040" xmlns="http://www.w3.org/2000/svg">
      <defs>
        <linearGradient id="siteTones" x1="0" y1="0" x2="0" y2="1">
          <stop offset="0" stop-color="var(--photo-sky)"/>
          <stop offset="0.55" stop-color="#8d8178"/>
          <stop offset="1" stop-color="var(--photo-ground)"/>
        </linearGradient>
      </defs>
      <!-- framing brackets around specialty text -->
      <polyline class="bracket-top" points="34,416 34,357 301,357" fill="none" stroke="var(--gold)" stroke-width="3"/>
      <polyline class="bracket-bottom" points="182,499 427,499 427,435" fill="none" stroke="var(--gold)" stroke-width="3"/>
      <!-- construction site photo area -->
      <polygon class="site-photo" role="img" aria-label="Photo of a commercial building under construction with steel framing and a dirt site"
        points="77,664 461,664 461,896 190,896" fill="url(#siteTones)"/>
      <!-- angular accents -->
      <polygon class="accent-stripe" points="44,664 72,664 170,800 142,800" fill="var(--gold)"/>
      <polyline class="accent-line" points="24,664 150,836 196,836" fill="none" stroke="var(--navy)" stroke-width="3"/>
      <polygon class="accent-block" points="0,828 58,752 90,776 0,892" fill="var(--gold)"/>
      <polygon class="footer-chevron" points="0,960 70,880 102,846 150,899 461,899 461,1040 0,1040" fill="var(--navy)"/>
    </svg>

    <header class="brand">
      <div class="brand-name">BRISOL</div>
      <div class="brand-tagline">Collaborative Construction</div>
    </header>

    <h1 class="headline">
      <span class="headline-top">Commercial</span>
      <span class="headline-bottom">Construction</span>
    </h1>

    <p class="specialty">
      <span class="specialty-light">Specializing in Historic<br>Renovation and</span><br>
      <span class="specialty-strong">Urban Development</span>
    </p>

    <p class="career-call">Start your career<br>in construction with<br>the creative team of Brisol</p>

    <p class="location">Downtown Jacksonville Florida</p>
  </section>
</div>
</body>
</html>
```